Speisekarten-Design für italienisches Restaurant im Golfclub mit Blick auf die Alpen
Zielgruppe
Italienisches Restaurant im Golfclub mit Blick auf die Alpen (bei gutem Wetter)
Aufgabenstellung
Karte muss weiterhin bearbeitet werden könne. Es geht um ein Design das optisch anspricht aber nicht übertrieben ist. Die Blätter kommen später in eine Menukarte die noch in Auftrag gegeben werden.
Im Idealfall kann der Designer hierfür auch was mit designen das an einen Firma weitergeben werden kann um die 'Umschläge zu erstellen. Logo kann muss nicht mit drin sein. Es geht auch sehr um die einfache Darstellung des Ganzen.

```html
<!DOCTYPE html>
<html lang="de">
<head>
<meta charset="utf-8">
<title>Ristorante Serralta – Menüs</title>
<link href="https://fonts.googleapis.com/css2?family=Roboto+Condensed:wght@700&family=Arimo:wght@400&family=Cormorant+Garamond:wght@600&display=swap" rel="stylesheet">
<style>
  :root {
    --night: #020233;
    --sand: #bcb29a;
    --frame: #8c8672;
    --gold: #c9a23f;
  }
  html, body {
    margin: 0;
    padding: 0;
    overflow: hidden;
  }
  .menu-sheet {
    position: relative;
    width: 735px;
    height: 1200px;
    background: var(--night);
    overflow: hidden;
    font-family: "Arimo", Arial, sans-serif;
    color: var(--sand);
  }
  .brand {
    position: absolute;
    left: 0;
    width: 735px;
    top: 52px;
    text-align: center;
  }
  .brand-name {
    font-family: "Cormorant Garamond", Georgia, serif;
    font-weight: 600;
    font-size: 34px;
    letter-spacing: 1px;
    color: var(--gold);
    line-height: 1.1;
    margin: 0;
  }
  .course-box, .price-box {
    position: absolute;
    border: 1px solid var(--frame);
    box-sizing: border-box;
  }
  .course-box { left: 69px; width: 403px; }
  .price-box { left: 498px; width: 168px; }
  .course-title {
    position: absolute;
    left: 17px;
    margin: 0;
    font-family: "Roboto Condensed", "Arial Narrow", sans-serif;
    font-weight: 700;
    font-size: 48px;
    line-height: 1;
    transform: scaleX(0.92);
    transform-origin: left;
  }
  .course-list {
    position: absolute;
    left: 15px;
    margin: 0;
    padding: 0;
    list-style: none;
    font-size: 13.2px;
    line-height: 31.7px;
  }
  .price {
    position: absolute;
    left: 32px;
    margin: 0;
    font-family: "Roboto Condensed", "Arial Narrow", sans-serif;
    font-weight: 700;
    font-size: 48px;
    line-height: 1;
    transform: scaleX(0.92);
    transform-origin: left;
  }
  .table-scene {
    position: absolute;
    left: 216px;
    top: 996px;
    width: 308px;
    height: 164px;
    background: radial-gradient(ellipse at center, #5d5a5a 0%, #2a2947 60%, var(--night) 100%);
  }
  .footer-band {
    position: absolute;
    left: 166px;
    top: 1170px;
    width: 403px;
    height: 30px;
    background: var(--sand);
  }
</style>
</head>
<body>
<main class="menu-sheet">
  <header class="brand">
    <p class="brand-name">Ristorante Serralta</p>
  </header>

  <section class="course-box" style="top:177px;height:240px;">
    <h2 class="course-title" style="top:22px;">MENU 1</h2>
    <ul class="course-list" style="top:75px;">
      <li>Appetithäppchen und Aperitif</li>
      <li>Italiensicher Aufschnitt Teller</li>
      <li>Pasta mit Hackfleischsoße und Sahne</li>
      <li>Kalbsbraten mit Barolosoße und Rosmarin Kartoffeln</li>
      <li>Zitronen Sorbet</li>
    </ul>
  </section>
  <div class="price-box" style="top:177px;height:240px;">
    <p class="price" style="top:98px;">49,-</p>
  </div>

  <section class="course-box" style="top:435px;height:222px;">
    <h2 class="course-title" style="top:22px;">MENU 2</h2>
    <ul class="course-list" style="top:75px;">
      <li>Gemischter Salat</li>
      <li>Pasta mit scharfer Tomatensoße</li>
      <li>Putengeschnetzeltes in Currysoße mit Reis</li>
      <li>Tiramisu</li>
    </ul>
  </section>
  <div class="price-box" style="top:435px;height:222px;">
    <p class="price" style="top:89px;">35,-</p>
  </div>

  <section class="course-box" style="top:676px;height:305px;">
    <h2 class="course-title" style="top:13px;">MENU 3</h2>
    <ul class="course-list" style="top:74px;">
      <li>Aperitif</li>
      <li>Vitello Tonnato</li>
      <li>Lasagne im Ofen überbacken</li>
      <li>Rumpsteak tranchiert, auf Rucola Bett serviert mit</li>
      <li>gehobelten Original Parmesan Käse</li>
      <li>Rosmarinkartoffeln und Gemüse</li>
      <li>Panna Cotta mit Waldfrüchte</li>
    </ul>
  </section>
  <div class="price-box" style="top:676px;height:305px;">
    <p class="price" style="top:132px;">55,-</p>
  </div>

  <div class="table-scene" role="img" aria-label="Illustration eines gedeckten runden Tisches mit zwei Bistrostühlen"></div>
  <div class="footer-band"></div>
</main>
</body>
</html>
```